Hooded Rogue - Game Company Site

Looking for a simple and sleek 3 page design for a game company site. Will provide a logo to be included in the design. Even though we specialize in flash games at the moment, we plan on expanding to other platforms and would like a site similar to console developer sites than flash game portals. Example: http://brightquill.example

Required Pages:
1. Home: advertising the latest game, big image, and possibly a news post
2. Games: a portfolio of games, each game will have a large image preview and some text, with a link to the game
3. About Us:
A roster of employees, each will have a picture and bio with name, alias, location, and some text.

Would be nice to have a theme inspired by "villains." The logo should provide the general feel we are looking for. You will find the logo attached as a .PSD (Photoshop) and a .PNG to give a quick preview. Vector .ai and .eps logos have also been attached. Feel free to split the text from the character or make any changes you feel necessary!

About Hooded Rogue
We create flash games and are hoping to expand to iPhone games and other platforms in the future!
Our latest game: http://www.plarvexa.example/games/quentloo/tabrin-quest-2-chapter-1

Target Market(s)

18-30 year old male tech and video game enthusiasts

Industry/Entity Type

Advertising

Requirements
Must have
• Must have the logo that is attached.

```html
<!DOCTYPE html>
<html lang="en">
<head>
<meta charset="utf-8">
<title>Hooded Rogue</title>
<link rel="stylesheet" href="https://fonts.googleapis.com/css2?family=Arimo:wght@400;700&family=Tinos:wght@700&display=swap">
<style>
  :root {
    --page-red: #e1290e;
    --frame-dark: #1a0a06;
    --ink: #111111;
    --brand-gold: #f6b51e;
    --card-frame: #ffffff;
    --card-text: #ff7a5c;
    --card-title: #ff6242;
    --field-red: #a90f12;
    --panel-light: #6e6e6e;
    --panel-dark: #000000;
    --thumb-light: #c9c9c9;
  }
  * { box-sizing: border-box; margin: 0; padding: 0; }
  html, body { width: 1097px; height: 1200px; overflow: hidden; }
  body {
    position: relative;
    background: var(--page-red);
    border: 3px solid var(--frame-dark);
    border-top-width: 6px;
    font-family: "Arimo", Arial, sans-serif;
    color: var(--ink);
  }
  .brand {
    position: absolute; left: 50px; top: 70px;
    display: flex; align-items: center; gap: 16px;
  }
  .brand-mark {
    width: 78px; height: 78px; border-radius: 50%;
    background: var(--brand-gold);
  }
  .brand-name {
    font-size: 38px; font-weight: 700; color: var(--ink);
  }
  .intro {
    position: absolute; left: 43px; top: 204px; width: 1036px;
    font-size: 16.3px; line-height: 22.6px;
  }
  .game-card {
    position: absolute; left: 24px; width: 1053px; height: 202px;
    background: var(--card-frame);
  }
  .game-card--one { top: 329px; }
  .game-card--two { top: 547px; }
  .game-card--three { top: 765px; }
  .game-thumb {
    position: absolute; left: 10px; top: 9px; width: 227px; height: 180px;
    background: linear-gradient(to right, var(--thumb-light), var(--panel-dark));
  }
  .game-panel {
    position: absolute; left: 243px; top: 9px; width: 799px; height: 180px;
    background: linear-gradient(to right, var(--panel-light), var(--panel-dark) 85%);
    color: var(--card-text);
    padding: 12px 8px 0 8px;
  }
  .game-name {
    font-family: "Tinos", "Times New Roman", serif;
    color: var(--card-title);
    font-size: 18px; font-weight: 700; line-height: 20px;
  }
  .game-tag { font-size: 15px; line-height: 20px; }
  .game-text {
    margin-top: 16px;
    font-size: 15.4px; line-height: 19px;
  }
  .search {
    position: absolute; left: 57px; top: 1004px;
    display: flex; align-items: center;
  }
  .search-label { font-size: 25px; color: var(--ink); margin-right: 20px; }
  .search-field {
    width: 225px; height: 36px;
    background: var(--field-red);
    border: 3px solid var(--card-frame);
  }
  .search-icon { margin-left: 14px; }
  .more-link {
    position: absolute; left: 966px; top: 1003px;
    font-size: 25px; color: var(--ink); text-decoration: none;
  }
  .copyright {
    position: absolute; left: 758px; top: 1160px;
    font-size: 16.5px; color: var(--ink); word-spacing: 2px;
  }
</style>
</head>
<body>
  <header class="brand">
    <span class="brand-mark"></span>
    <span class="brand-name">Hooded Rogue</span>
  </header>

  <p class="intro">Lorem ipsum dolor sit amet, cons ectetur adipisicing elit, sed do eiusmod tempor&nbsp; incididunt ut labore et dolore magna aliqua. Ut enimad minim veniam, quis nostrud exercitation test link ullamco laboris nisi ut aliquip ex ea commodo consequat. Duis au te irure dolor in reprehenderit in voluptate another link velit esse cillum dolore eu fugiat nulla pariatur. Excepteur sint occaecat cupidatat non proident, sunt in culpa qui officia deserunt mollit anim id est laborum.</p>

  <article class="game-card game-card--one">
    <div class="game-thumb" role="img" aria-label="Team member portrait"></div>
    <div class="game-panel">
      <h2 class="game-name">NAME</h2>
      <p class="game-tag">est laborum</p>
      <p class="game-text">Lorem ipsum dolor sit amet, cons ectetur adipisicing elit, sed do eiusmod tempor&nbsp; incididunt ut labore et dolore magna aliqua. Ut enimad minim veniam, quis nostrud exercitation test link ulla mco laboris nisi ut aliquip ex ea commodo consequat. Duis aute irure dolor in reprehenderit in voluptate another link velit esse cillum dolore eu fugiat nulla pariatur. Excepteur sint occaecat cupidatat non proident, sunt in culpa qui officia deserunt mollit anim id est laborum.</p>
    </div>
  </article>

  <article class="game-card game-card--two">
    <div class="game-thumb" role="img" aria-label="Team member portrait"></div>
    <div class="game-panel">
      <h2 class="game-name">NAME</h2>
      <p class="game-tag">est laborum</p>
      <p class="game-text">Lorem ipsum dolor sit amet, cons ectetur adipisicing elit, sed do eiusmod tempor&nbsp; incididunt ut labore et dolore magna aliqua. Ut enimad minim veniam, quis nostrud exercitation test link ulla mco laboris nisi ut aliquip ex ea commodo consequat. Duis aute irure dolor in reprehenderit in voluptate another link velit esse cillum dolore eu fugiat nulla pariatur. Excepteur sint occaecat cupidatat non proident, sunt in culpa qui officia deserunt mollit anim id est laborum.</p>
    </div>
  </article>

  <article class="game-card game-card--three">
    <div class="game-thumb" role="img" aria-label="Team member portrait"></div>
    <div class="game-panel">
      <h2 class="game-name">NAME</h2>
      <p class="game-tag">est laborum</p>
      <p class="game-text">Lorem ipsum dolor sit amet, cons ectetur adipisicing elit, sed do eiusmod tempor&nbsp; incididunt ut labore et dolore magna aliqua. Ut enimad minim veniam, quis nostrud exercitation test link ulla mco laboris nisi ut aliquip ex ea commodo consequat. Duis aute irure dolor in reprehenderit in voluptate another link velit esse cillum dolore eu fugiat nulla pariatur. Excepteur sint occaecat cupidatat non proident, sunt in culpa qui officia deserunt mollit anim id est laborum.</p>
    </div>
  </article>

  <form class="search">
    <span class="search-label">SEARCH</span>
    <span class="search-field"></span>
    <svg class="search-icon" width="44" height="44" viewBox="0 0 44 44" aria-hidden="true">
      <circle cx="16" cy="16" r="11" fill="#e8e8e8" stroke="#ffffff" stroke-width="4"/>
      <line x1="24" y1="24" x2="38" y2="38" stroke="#ffffff" stroke-width="7" stroke-linecap="round"/>
    </svg>
  </form>

  <a class="more-link" href="#">more &gt;&gt;</a>

  <footer class="copyright">Copyright © 2011 &nbsp;&nbsp;All rights reserved.</footer>
</body>
</html>
```